会社や店舗の収支を毎日把握管理することで、販売、労務、キャッシュフローの管理が毎日出来るシステムです。
現在複数の地方銀行とのビジネスマッチングが進んでおり、今回のチラシは、銀行の渉外担当者が、顧客先にて置いてくるチラシです。その後、顧客より興味がある等レスがあった際はこちらから連絡して契約につなげます。
ですので、このシステムのことが理解出来ていない、銀行員や顧客でもまずはA4の表裏で興味を持ってもらえて問い合わせがもらえることが目的のものです。
今後銀行ごとにオリジナルのデザインの要望が来ることも考えられ、その際は継続的に仕事を依頼する予定です。
デザインの変わらない項目などの変更程度は納品後も対応頂ける方がありがたいです。もちろんデザインが変わる際は別途報酬をお支払いします。

```html
<!DOCTYPE html>
<html lang="ja">
<head>
<meta charset="utf-8">
<title>snap log 導入のご案内</title>
<link rel="stylesheet" href="https://fonts.googleapis.com/css2?family=Noto+Sans+JP:wght@400;500;700;900&display=swap">
<style>
:root{
  --blue:#1f5fd8;
  --blue-dark:#163f9c;
  --sky:#28a8e8;
  --pale:#e9f3fb;
  --grey-bg:#eceef1;
  --grey:#c9cdd3;
  --ink:#222;
  --yellow:#fff07a;
  --gold:#f7e15a;
  --red:#e8242c;
  --accent:#ff4b1f;
}
*{box-sizing:border-box;margin:0;padding:0}
html,body{width:849px;height:1200px;overflow:hidden;background:#fff}
body{font-family:"Noto Sans JP",sans-serif;color:var(--ink);position:relative}
.flyer{position:relative;width:849px;height:1200px;overflow:hidden}

/* worries */
.worries{position:absolute;left:0;top:0;width:849px;height:470px;background:var(--grey-bg)}
.worries-title{position:absolute;left:190px;top:0;width:470px;height:44px;background:var(--blue);color:#fff;font-weight:700;font-size:19px;display:flex;align-items:center;justify-content:center;letter-spacing:.08em}
.panel{position:absolute;top:62px;width:385px;height:393px;background:#fff}
.panel.owner{left:25px}
.panel.staff{left:439px}
.panel-head{margin:14px auto 0;width:200px;text-align:center;color:var(--blue-dark);font-weight:700;font-size:17px;border-bottom:2px solid var(--blue-dark);padding-bottom:4px}
.panel ul{list-style:none;margin:14px 22px 0;font-size:12px;line-height:1.6}
.panel li{padding-left:1.1em;text-indent:-1.1em;margin-bottom:6px}
.panel li::before{content:"■";color:var(--blue)}
.bubble{position:absolute;width:120px;height:120px;border-radius:50%;background:#dcdfe4;display:flex;align-items:center;justify-content:center;text-align:center;font-size:11px;line-height:1.5;font-weight:500;padding:14px}
.owner .bubble{left:112px;top:240px}
.staff .bubble{left:150px;top:240px}
.figure{position:absolute;background:linear-gradient(#d7dbe1,#aeb4bd)}
.owner .figure{left:250px;top:222px;width:100px;height:160px}
.staff .figure{left:270px;top:250px;width:100px;height:130px}

/* headline band */
.headline{position:absolute;left:0;top:470px;width:849px;height:180px}
.headline svg{position:absolute;left:0;top:0}
.headline .lead{position:absolute;left:0;width:849px;top:40px;text-align:center;color:#fff;font-size:26px;font-weight:700}
.headline .main{position:absolute;left:0;width:849px;top:88px;text-align:center;color:#fff;font-size:42px;font-weight:900;letter-spacing:.02em}
.headline .main em{font-style:normal;color:var(--accent)}

/* plans */
.plans{position:absolute;left:40px;top:660px;width:770px;display:flex;justify-content:space-between}
.plan{width:240px}
.plan-head{background:var(--sky);color:#fff;text-align:center;padding:5px 0 4px;border:2px solid #fff;outline:2px solid var(--sky)}
.plan-price{color:var(--yellow);font-weight:900;font-size:19px;line-height:1.25}
.plan-name{font-weight:900;font-size:19px;line-height:1.25}
.plan ul{list-style:none;background:var(--pale);padding:6px;text-align:center;font-size:10.5px;line-height:1.4;height:116px}
.plan li.hl{color:var(--red)}
.note{position:absolute;right:40px;top:843px;color:var(--red);font-size:11px;line-height:1.3}

/* flow */
.flow-bar{position:absolute;left:0;top:866px;width:849px;height:30px}
.flow-bar span{position:absolute;top:4px;color:#fff;font-size:13px;font-weight:700}
.steps{position:absolute;left:22px;top:908px;width:805px;display:flex;justify-content:space-between;align-items:center}
.step{width:70px;height:70px;border-radius:50%;background:var(--gold);display:flex;align-items:center;justify-content:center;text-align:center;font-weight:700;font-size:15px;line-height:1.2}
.step-arrow{width:0;height:0;border-top:7px solid transparent;border-bottom:7px solid transparent;border-left:10px solid var(--gold)}

/* contact */
.contact-rule{position:absolute;left:25px;top:1000px;width:800px;height:3px;background:var(--blue)}
.company{position:absolute;left:60px;top:1020px;font-size:29px;font-weight:900;color:var(--blue-dark)}
.phone{position:absolute;left:60px;top:1058px;font-size:44px;font-weight:900;color:var(--blue-dark);letter-spacing:.02em;display:flex;align-items:center;gap:10px}
.address{position:absolute;left:60px;top:1128px;font-size:15px;line-height:1.9}
.inquiry{position:absolute;left:575px;top:1018px;width:150px;height:64px;background:#e3e6ea;border-radius:10px;font-size:15px;font-weight:700;display:flex;align-items:center;justify-content:center;text-align:center;line-height:1.4}
.handshake{position:absolute;left:735px;top:1005px;width:95px;height:100px;background:linear-gradient(#d5d9df,#9aa1ab)}
.brand{position:absolute;left:735px;top:1130px;width:100px;display:flex;flex-direction:column;align-items:center;gap:4px;color:var(--blue-dark);font-weight:700;font-size:10px}
.brand i{display:block;width:26px;height:26px;background:var(--blue-dark)}
</style>
</head>
<body>
<main class="flyer">

  <section class="worries">
    <h2 class="worries-title">経営分析・財務分析でよくある悩み</h2>

    <div class="panel owner">
      <h3 class="panel-head">経営者の悩み</h3>
      <ul>
        <li>レポート作成に時間がかかり、データの更新が遅れて判断に間に合わない</li>
        <li>数字を見てもどこに問題があるのかすぐに分からない</li>
        <li>最新の売上や資金の状況を毎日つかめる仕組みがほしい</li>
      </ul>
      <div class="bubble">タイムリーに<br>経営状況を把握<br>できるシステム<br>が必要!</div>
      <div class="figure" role="img" aria-label="腕を組んで考える経営者のシルエット"></div>
    </div>

    <div class="panel staff">
      <h3 class="panel-head">担当者の悩み</h3>
      <ul>
        <li>集計作業が毎回手作業で、入力ミスや確認に追われている</li>
        <li>複数の表を行き来して、資料づくりに時間がかかる</li>
        <li>いろいろな数字をまとめて見られる仕組みがなく不便</li>
      </ul>
      <div class="bubble">使いやすくて<br>手間なく分析<br>できるシステム<br>が欲しい!</div>
      <div class="figure" role="img" aria-label="パソコンで作業する担当者のシルエット"></div>
    </div>
  </section>

  <section class="headline">
    <svg width="849" height="180" viewBox="0 0 849 180" aria-hidden="true">
      <polygon points="0,0 849,0 849,150 0,180" fill="var(--blue)"/>
    </svg>
    <p class="lead">snap logで</p>
    <p class="main">集計・分析・管理業務が<em>劇的変化!</em></p>
  </section>

  <section class="plans">
    <article class="plan">
      <div class="plan-head">
        <div class="plan-price">月額54,800円</div>
        <div class="plan-name">snap log</div>
      </div>
      <ul>
        <li>販売システム連携</li>
        <li>分析アカウント発行</li>
        <li>集計表の自動作成</li>
        <li>日次レポート配信</li>
        <li>各種設定サポート</li>
      </ul>
    </article>
    <article class="plan">
      <div class="plan-head">
        <div class="plan-price">月額59,800円</div>
        <div class="plan-name">snap log プラス</div>
      </div>
      <ul>
        <li>販売・勤怠システム連携</li>
        <li>分析アカウント発行</li>
        <li>集計表の自動作成</li>
        <li>日次レポート配信</li>
        <li>変更サポート対応</li>
        <li class="hl">スタッフの人件費分析</li>
      </ul>
    </article>
    <article class="plan">
      <div class="plan-head">
        <div class="plan-price">月額59,800円</div>
        <div class="plan-name">snap log セールス</div>
      </div>
      <ul>
        <li>販売・在庫システム連携</li>
        <li>分析アカウント発行</li>
        <li>集計表の自動作成</li>
        <li>日次レポート配信</li>
        <li>変更サポート対応</li>
        <li class="hl">スタッフ別売上分析</li>
        <li class="hl">在庫管理システム連携</li>
      </ul>
    </article>
  </section>
  <p class="note">※3店舗目までの月額料金です</p>

  <section class="flow">
    <div class="flow-bar">
      <svg width="849" height="30" viewBox="0 0 849 30" aria-hidden="true">
        <polygon points="25,0 420,0 432,15 420,30 25,30" fill="var(--blue)"/>
        <polygon points="436,0 600,0 612,15 600,30 436,30 448,15" fill="var(--blue)"/>
        <polygon points="616,0 825,0 825,30 616,30 628,15" fill="#8fa9d8"/>
      </svg>
      <span style="left:200px">5営業日</span>
      <span style="left:495px">5営業日</span>
      <span style="left:690px">利用開始</span>
    </div>
    <div class="steps">
      <div class="step">契約</div><div class="step-arrow"></div>
      <div class="step">39<br>コール</div><div class="step-arrow"></div>
      <div class="step">打合せ</div><div class="step-arrow"></div>
      <div class="step">制作</div><div class="step-arrow"></div>
      <div class="step">内容<br>確認</div><div class="step-arrow"></div>
      <div class="step">引渡し</div><div class="step-arrow"></div>
      <div class="step">検収</div>
    </div>
  </section>

  <footer class="contact">
    <div class="contact-rule"></div>
    <p class="company">株式会社　帳簿ワークス</p>
    <p class="phone">
      <svg width="36" height="36" viewBox="0 0 24 24" aria-hidden="true"><path fill="var(--blue-dark)" d="M6.6 10.8a15.1 15.1 0 0 0 6.6 6.6l2.2-2.2c.3-.3.7-.4 1-.2 1.1.4 2.3.6 3.6.6.6 0 1 .4 1 1V20c0 .6-.4 1-1 1A17 17 0 0 1 3 4c0-.6.4-1 1-1h3.5c.6 0 1 .4 1 1 0 1.3.2 2.5.6 3.6.1.3 0 .7-.2 1z"/></svg>
      052-000-1234
    </p>
    <p class="address">本社：460-0000　愛知県名古屋市中区栄町1-2-3<br>支店：680-0000　鳥取県鳥取市本町2-4-5</p>
    <div class="inquiry">お気軽に<br>お問い合わせください</div>
    <div class="handshake" role="img" aria-label="握手するビジネスパーソンのシルエット"></div>
    <div class="brand"><i></i><span>CHOBO WORKS</span></div>
  </footer>

</main>
</body>
</html>
```